Wedding Thank You post card

We would like to design a thank you post card for our wedding guests.
We want it to be a classic style with our photo and a simple 'Thank you' written and then Tom and Sylvia 15.03.2014' Where the writing does not obstruct our image.
We need 140 post cards
Sorry for the delay please find some photos you can use for the design process. One or all photos can be used. Thank you
Wedding

```html
<!DOCTYPE html>
<html lang="en">
<head>
<meta charset="utf-8">
<title>Tom and Sylvia – Thank You Postcard</title>
<link rel="stylesheet" href="https://fonts.googleapis.com/css2?family=Federo&family=Delius+Unicase:wght@400;700&family=Pinyon+Script&display=swap">
<style>
  :root {
    --backdrop: #000000;
    --front-brown: #5a4d45;
    --photo-mat: #ffffff;
    --cream: #e6e1d0;
    --ink-brown: #6a5144;
    --stamp-brown: #7a5f52;
    --line-brown: #5e4a3f;
    --light-text: #f4efe6;
  }
  * { margin: 0; padding: 0; box-sizing: border-box; }
  html, body { width: 781px; height: 1200px; overflow: hidden; background: var(--backdrop); }
  .canvas { position: relative; width: 781px; height: 1200px; }

  .card-front {
    position: absolute; left: 32px; top: 29px; width: 720px; height: 559px;
    background: var(--front-brown);
  }
  .front-title {
    position: absolute; left: 30px; top: 100px;
    font-family: "Pinyon Script", cursive; font-size: 44px; color: var(--light-text);
    letter-spacing: 1px;
  }
  .photo-band {
    position: absolute; left: 4px; top: 184px; width: 716px; height: 243px;
    background: var(--photo-mat);
  }
  .photo-band svg { display: block; }
  .couple-names, .couple-date {
    position: absolute; left: 0; width: 100%; text-align: center;
    font-family: "Federo", sans-serif; color: var(--light-text);
  }
  .couple-names { top: 441px; font-size: 31px; letter-spacing: 1px; }
  .couple-date { top: 484px; font-size: 29px; }

  .card-back {
    position: absolute; left: 32px; top: 610px; width: 720px; height: 560px;
    background: var(--cream);
  }
  .card-back svg.frame { position: absolute; left: 0; top: 0; }
  .stamp-box {
    position: absolute; left: 542px; top: 18px; width: 160px; height: 162px;
    background: var(--stamp-brown);
  }
  .back-names {
    position: absolute; left: 55px; top: 100px;
    font-family: "Delius Unicase", sans-serif; font-weight: 700; font-size: 25px;
    color: var(--ink-brown); letter-spacing: 1px;
  }
  .back-date {
    position: absolute; left: 55px; top: 142px; width: 256px; text-align: center;
    font-family: "Delius Unicase", sans-serif; font-weight: 700; font-size: 23px;
    color: var(--ink-brown);
  }
  .thanks-message {
    position: absolute; left: 48px; top: 200px; width: 290px;
    font-family: "Delius Unicase", sans-serif; font-size: 18.5px; line-height: 36px;
    color: var(--ink-brown);
  }
</style>
</head>
<body>
<main class="canvas">
  <section class="card-front">
    <div class="front-title">THANK YOU....</div>
    <div class="photo-band">
      <svg width="716" height="243" viewBox="0 0 716 243">
        <defs>
          <linearGradient id="sky-water" x1="0" y1="0" x2="0" y2="1">
            <stop offset="0" stop-color="#dfe4e6"/>
            <stop offset="1" stop-color="#b9a79c"/>
          </linearGradient>
        </defs>
        <g class="collage" role="img" aria-label="Photo collage of the bride and groom walking arm in arm down a tree-lined path">
          <rect x="15" y="3" width="126" height="113" fill="#5f6b52"/>
          <rect x="148" y="3" width="87" height="113" fill="#8d8a7e"/>
          <rect x="241" y="3" width="127" height="113" fill="#4c5a5c"/>
          <rect x="15" y="124" width="126" height="116" fill="#8a6a80"/>
          <rect x="148" y="124" width="87" height="116" fill="#a79b8d"/>
          <rect x="241" y="124" width="127" height="116" fill="#8f9a55"/>
        </g>
        <rect class="portrait" x="388" y="3" width="307" height="237" fill="url(#sky-water)" role="img" aria-label="Photo of the bride holding a white bouquet beside the groom by the water"/>
      </svg>
    </div>
    <div class="couple-names">TOM AND SYLVIA</div>
    <div class="couple-date">15.03.2014</div>
  </section>

  <section class="card-back">
    <svg class="frame" width="720" height="560" viewBox="0 0 720 560">
      <g stroke="var(--line-brown)" stroke-width="3" stroke-dasharray="2 6" fill="none" stroke-linecap="round">
        <line x1="60" y1="18" x2="530" y2="18"/>
        <line x1="19" y1="60" x2="19" y2="490"/>
        <line x1="704" y1="200" x2="704" y2="490"/>
        <line x1="60" y1="540" x2="650" y2="540"/>
        <line x1="340" y1="183" x2="340" y2="460"/>
        <line x1="346" y1="183" x2="346" y2="460"/>
      </g>
      <g stroke="var(--line-brown)" stroke-width="3">
        <line x1="369" y1="244" x2="681" y2="244"/>
        <line x1="369" y1="287" x2="681" y2="287"/>
        <line x1="369" y1="330" x2="681" y2="330"/>
        <line x1="369" y1="374" x2="681" y2="374"/>
        <line x1="369" y1="416" x2="681" y2="416"/>
      </g>
    </svg>
    <div class="stamp-box"></div>
    <div class="back-names">TOM AND SYLVIA</div>
    <div class="back-date">15.03.2014</div>
    <p class="thanks-message">Thank God that we have friends like you! Your kindness and presence, your big and open hearts made our wedding day never-to-be-forgotten.</p>
  </section>
</main>
</body>
</html>
```